Wrenmoor Learning Houses MOXIE Poster

We need a poster to put up around our Community/Youth Centers that shows the acronym M.O.X.I.E. which stands for the traits our that make up the culture and personalities of our youth, families and staff. We would like the color scheme to be in our brand colors, and will send them as an upload (grey, blue, green). The poster must have our logo & tagline (uploaded), which may be small and not central. It should have the acronym with the associated words spelled out - as the smaller descriptive words as shown in uploaded attachment. It should be fun - youth friendly (ages 3-18) and really pop. I have also uploaded a sample poster that we created - but don't like....it feels boring, uninspired. It must say "The WLH" M.O.X.I.E as MOXIE is also the name of a different youth agency and we don't want our acronym to be confused with their name. Finally - to tell you a bit more about our organization I have uploaded our annual report. We can't way to see your ideas!!

Target Market(s)

Internal Information Poster for our community centers

Industry/Entity Type

Education

Font styles to use
Other font styles liked:
• FUN

Requirements
Must have
• It must say "The WLH" M.O.X.I.E as MOXIE is also the name of a different youth agency and we don't want our acronym to be confused with their name
• The WLH M.O.X.I.E. - and associated words - should be dominant/prevalent ....
Nice to have
• Fun Images/photos of actual sparks....
Should not have
• As described w/uploads

```html
<!DOCTYPE html>
<html lang="en">
<head>
<meta charset="utf-8">
<title>The WLH MOXIE Poster</title>
<link rel="stylesheet" href="https://fonts.googleapis.com/css2?family=Fredoka:wght@500;600;700&display=swap">
<style>
  :root {
    --ink: #3a3b3d;
    --ray-light: #f4fbef;
    --ray-mid: #b9df9a;
    --ray-deep: #4fa83a;
    --sky-soft: #97d7e9;
    --sky-text: #2a8d92;
    --teal: #4dbfbe;
    --teal-letter: #8fd4e6;
    --teal-word: #1d5b5c;
    --leaf-soft: #c0e09d;
    --leaf-text: #4ea63c;
    --leaf: #6fbb45;
    --leaf-letter: #b9dd97;
    --leaf-word: #2b6a2c;
    --stone-soft: #b3b4b7;
    --stone-text: #3e3f41;
    --stone: #8f9094;
    --stone-letter: #b8b9bc;
    --stone-word: #3b3c3e;
    --footer-bg: #ffffff;
    --footer-name: #7d7f83;
  }
  * { box-sizing: border-box; margin: 0; padding: 0; }
  html, body { width: 877px; height: 1200px; overflow: hidden; background: #fff; }
  .poster { width: 877px; height: 1200px; display: flex; flex-direction: column; font-family: "Fredoka", sans-serif; }

  .header { position: relative; height: 212px; overflow: hidden; }
  .header-rays {
    position: absolute; inset: 0;
    background:
      radial-gradient(ellipse at 50% 85%, var(--ray-light) 0%, rgba(244,251,239,0.9) 30%, rgba(185,223,154,0.6) 60%, transparent 85%),
      linear-gradient(180deg, var(--ray-deep) 0%, var(--ray-mid) 55%, var(--ray-light) 100%);
  }
  .title {
    position: relative; text-align: center; font-weight: 700; font-size: 150px; line-height: 1;
    color: var(--ink); letter-spacing: 2px; padding-top: 40px;
  }

  .trait { display: flex; height: 175px; }
  .trait-notes {
    width: 285px; padding: 40px 0 0 48px; font-weight: 600;
    font-size: 21px; line-height: 25px;
  }
  .trait-word { flex: 1; position: relative; }
  .initial {
    position: absolute; left: 58px; top: 2px; font-weight: 700; font-size: 182px; line-height: 1;
  }
  .rest {
    position: absolute; left: 196px; bottom: 14px; font-weight: 700; font-size: 56px; line-height: 1;
  }

  .trait--sky .trait-notes { background: var(--sky-soft); color: var(--sky-text); }
  .trait--sky .trait-word { background: var(--teal); }
  .trait--sky .initial { color: var(--teal-letter); }
  .trait--sky .rest { color: var(--teal-word); }

  .trait--leaf .trait-notes { background: var(--leaf-soft); color: var(--leaf-text); }
  .trait--leaf .trait-word { background: var(--leaf); }
  .trait--leaf .initial { color: var(--leaf-letter); }
  .trait--leaf .rest { color: var(--leaf-word); }

  .trait--stone .trait-notes { background: var(--stone-soft); color: var(--stone-text); }
  .trait--stone .trait-word { background: var(--stone); }
  .trait--stone .initial { color: var(--stone-letter); }
  .trait--stone .rest { color: var(--stone-word); }

  .footer {
    flex: 1; background: var(--footer-bg); display: flex; align-items: center; justify-content: center;
  }
  .brand-name {
    font-family: "Fredoka", sans-serif; font-size: 34px; font-weight: 600;
    color: var(--footer-name); letter-spacing: 0.5px; line-height: 1;
  }
</style>
</head>
<body>
<main class="poster">
  <header class="header">
    <div class="header-rays" role="img" aria-label="Bright green light rays bursting from a glowing centre with tiny sparkles"></div>
    <h1 class="title">The WLH</h1>
  </header>

  <section class="trait trait--sky">
    <div class="trait-notes">Warm &amp; Welcoming<br>Confident<br>Communicator<br>Positive Attitude</div>
    <div class="trait-word"><span class="initial">M</span><span class="rest">erry</span></div>
  </section>

  <section class="trait trait--leaf">
    <div class="trait-notes">Persistent Goal<br>Oriented Engaged<br>Creative Innovator</div>
    <div class="trait-word"><span class="initial">O</span><span class="rest">ptimistic</span></div>
  </section>

  <section class="trait trait--stone">
    <div class="trait-notes">Resilient<br>Resourceful<br>Willing<br>Critical Thinker</div>
    <div class="trait-word"><span class="initial">X</span><span class="rest">tra Adaptable</span></div>
  </section>

  <section class="trait trait--sky">
    <div class="trait-notes">Accountable<br>Committed<br>Self-Regulating</div>
    <div class="trait-word"><span class="initial">I</span><span class="rest">nvested</span></div>
  </section>

  <section class="trait trait--leaf">
    <div class="trait-notes">Empathetic<br>Collaborative<br>Helpful</div>
    <div class="trait-word"><span class="initial">E</span><span class="rest">ncouraging</span></div>
  </section>

  <footer class="footer">
    <div class="brand-name">WRENMOOR LEARNING HOUSES</div>
  </footer>
</main>
</body>
</html>
```